Help us Create Excitement with a Food To Go Web Site Menu

We are seeking a design that can serve as a template for a Wordpress based website. The template will present the name (BrimBowl), present the menu items with price details, and contact details. The final design should NOT have the Mingle Kerb Eats subtitle anywhere in the site.
Our plan is to have the menu with basic graphic elements with the options to link to images/pictures of the menu item (perhaps linked via Instagram or something like that if possible).
Updates

Target Market(s)

Home dining menu intended to offer perspective customers an understanding of what they will be enjoying.

Contact Information for Business Card

BrimBowl logo (without the Mingle Kerb Eats tag line included)
hi@brimbowl.com.au
Phone: XXXX XXX XXX (to be provided)

Coding

Coded - Design and coding required

Number of Pages Required

2 page

Requirements
Must have
• A bold and colourful presence that is also on the playful side.

A clearly readable menu layout that doesn't feel small based on the limited number of items that we offer at this time.
Nice to have
• A playful semi-graffiti based feel would be nice to convey a sense of playfulness.
Should not have
• The design should not have an overly Asian feel to it.

It appears many people are misreading the brief so I am adding this point to clarify one of the design requirements.
-- The final design should NOT have the Mingle Kerb Eats subtitle anywhere in the site, including the logo.

```html
<!DOCTYPE html>
<html lang="en">
<head>
<meta charset="utf-8">
<title>BrimBowl</title>
<link rel="stylesheet" href="https://fonts.googleapis.com/css2?family=Montserrat:wght@400;600;700;800&family=Lato:wght@400;700&display=swap">
<style>
:root{
  --red:#d40f0f;
  --deep-red:#a30000;
  --black:#0b0b0b;
  --ink:#222;
  --grey:#6a6a6a;
  --rule:#dcdcdc;
  --white:#fff;
  --photo-pho:#3b3531;
  --photo-rolls:#6b7a56;
  --photo-crab:#d8b06a;
  --photo-sandwich:#e4d3b6;
}
*{box-sizing:border-box;margin:0;padding:0}
html,body{width:1200px;height:3907px;overflow:hidden}
body{position:relative;background:var(--white);font-family:"Lato",sans-serif;color:var(--ink)}
.abs{position:absolute}

/* header */
.site-header{left:0;top:0;width:1200px;height:103px;background:var(--black)}
.brand{left:76px;top:30px;font-family:"Montserrat",sans-serif;font-weight:800;font-size:34px;color:var(--red);letter-spacing:1px}
.main-nav{right:90px;top:44px;display:flex;gap:35px;font-family:"Montserrat",sans-serif;font-size:15px;color:var(--white)}
.main-nav .active{color:var(--red);font-weight:700;position:relative}
.main-nav .active::after{content:"";position:absolute;left:0;right:0;top:30px;height:2px;background:var(--white)}

/* hero */
.hero{left:0;top:103px;width:1200px;height:654px;
  background:linear-gradient(100deg,#242322 0%,#2c2825 40%,#4a3620 70%,#3a2e22 100%)}
.hero-copy{left:223px;top:280px;width:380px;color:var(--white)}
.hero-copy h1{font-family:"Montserrat",sans-serif;font-weight:700;font-size:44px;line-height:1.1}
.hero-copy p{font-family:"Montserrat",sans-serif;font-size:19px;line-height:22px;margin-top:14px}
.ghost-btn{left:221px;top:434px;width:178px;height:42px;border:2px solid var(--white);border-radius:21px;
  color:var(--white);font-family:"Montserrat",sans-serif;font-size:17px;display:flex;align-items:center;justify-content:center}
.dots{left:240px;top:505px;display:flex;gap:22px}
.dots span{width:16px;height:16px;border-radius:50%;background:var(--white)}
.dots span.hollow{background:transparent;border:4px solid var(--white)}

/* about */
.about{left:0;top:757px;width:1200px;height:206px;border-bottom:1px solid var(--rule)}
.about h2{left:75px;top:66px;font-family:"Montserrat",sans-serif;font-weight:800;font-size:46px;line-height:54px;color:var(--black)}
.about h2 span{display:block;color:var(--red);font-weight:400;font-size:40px}
.about p{left:341px;top:68px;width:540px;font-family:"Montserrat",sans-serif;font-size:15px;line-height:22px;color:#333}
.solid-btn{left:929px;top:76px;width:180px;height:42px;border-radius:21px;
  background:linear-gradient(90deg,var(--red),#7a0000);color:var(--white);
  font-family:"Montserrat",sans-serif;font-size:17px;display:flex;align-items:center;justify-content:center}

.section-title{left:0;width:1200px;top:1018px;text-align:center;font-family:"Montserrat",sans-serif;font-weight:800;font-size:47px;color:var(--black)}
.section-title span{color:var(--red);font-weight:400}

/* menu items */
.dish-frame{width:510px;height:341px;background:var(--deep-red);padding:14px}
.dish-frame .photo{width:100%;height:100%;border:4px solid var(--white)}
.dish{width:420px}
.dish h3{font-family:"Montserrat",sans-serif;font-weight:700;font-size:25px;color:#6b6b6b;letter-spacing:.3px}
.dish h3 small{font-weight:400;font-size:17px;color:var(--grey);letter-spacing:0}
.dish .price{font-family:"Montserrat",sans-serif;font-weight:600;font-size:38px;color:var(--red);margin-top:4px;padding-bottom:14px;border-bottom:1px solid var(--rule)}
.dish .price small{font-size:15px;font-weight:400;margin-left:6px}
.dish .price .note{font-size:21px;font-weight:400}
.dish p{font-size:14px;line-height:22px;color:#333;margin-top:20px}
.order-btn{margin-top:30px;width:180px;height:42px;border:1px solid var(--red);border-radius:21px;display:flex;align-items:center;
  justify-content:space-between;padding-left:16px;font-family:"Montserrat",sans-serif;font-weight:700;font-size:13px;color:var(--red)}
.order-btn i{width:52px;height:42px;border-radius:21px;background:var(--deep-red);display:flex;align-items:center;justify-content:center;margin-right:-1px}

/* contact */
.contact{left:0;top:3124px;width:1200px;height:449px;
  background:linear-gradient(100deg,#2a2620 0%,#3a3428 50%,#221f1b 100%);text-align:center;color:var(--white)}
.contact h2{margin-top:135px;font-family:"Montserrat",sans-serif;font-weight:800;font-size:47px}
.contact h2 span{color:var(--red);font-weight:400}
.contact h3{margin-top:22px;font-family:"Montserrat",sans-serif;font-weight:400;font-size:32px}
.contact a{display:inline-block;margin-top:6px;font-family:"Montserrat",sans-serif;font-size:32px;color:var(--red);text-decoration:underline}

/* footer */
.foot-brand{left:0;width:1200px;top:3622px;text-align:center;font-family:"Montserrat",sans-serif;font-weight:800;font-size:36px;color:var(--red)}
.foot-nav{left:0;width:1200px;top:3716px;display:flex;justify-content:center;gap:35px;font-family:"Montserrat",sans-serif;font-size:15px;color:#333}
.foot-nav .active{font-weight:700;color:var(--black)}
.social{left:0;width:1200px;top:3776px;display:flex;justify-content:center;gap:27px}
.social span{width:24px;height:24px;border-radius:50%;background:#1a1a1a}
.copyright{left:0;width:1200px;top:3830px;text-align:center;font-family:"Montserrat",sans-serif;font-size:15px;color:#333}
</style>
</head>
<body>

<header class="site-header abs">
  <div class="brand abs">BrimBowl</div>
  <nav class="main-nav abs">
    <span class="active">Home</span><span>About Us</span><span>Menus</span><span>Blog</span><span>FAQ</span><span>Contact Us</span>
  </nav>
</header>

<section class="hero abs" role="img" aria-label="Photo of crispy spring rolls on a rustic plate with chilli dipping sauce">
</section>
<div class="hero-copy abs">
  <h1>Lorium ipsum</h1>
  <p>Sed ut perspiciatis unde omnis iste natus error sit voluptatem accusantium doloremque laudantium,</p>
</div>
<div class="ghost-btn abs">LEARN MORE</div>
<div class="dots abs"><span></span><span class="hollow"></span><span></span></div>

<section class="about abs">
  <h2 class="abs">ABOUT<span>BRIMBOWL</span></h2>
  <p class="abs">Sed ut perspiciatis unde omnis iste natus error sit voluptatem accusantium doloremque laudantium, totam rem aperiam, eaque ipsa quae ab illo inventore veritatis et quasi architecto beatae vitae dicta sunt explicabo.</p>
  <div class="solid-btn abs">LEARN MORE</div>
</section>

<h2 class="section-title abs">OUR <span>MENUS</span></h2>

<!-- Pho -->
<div class="dish-frame abs" style="left:74px;top:1148px">
  <div class="photo" role="img" aria-label="Photo of a bowl of beef noodle soup" style="background:var(--photo-pho)"></div>
</div>
<div class="dish abs" style="left:674px;top:1163px">
  <h3>PHO<small>(beef noodle soup)</small></h3>
  <div class="price">$14</div>
  <p>Just like Ba (Grandma) used to make. Our Pho takes 12 hours to make. We boil and reduce our own broth, using the freshest, locally sourced ingredients. We use real beef filet, brisket, and Vietnamese meatballs paired with crispy beansprouts, green onion, cilantro, and Asian basil. We provide Hoisin and Sriracha (hot sauce) to create your perfect fusion of flavours.</p>
  <div class="order-btn">ADD TO ORDER<i><svg width="16" height="14" viewBox="0 0 16 14" fill="none" stroke="#fff" stroke-width="1.4"><path d="M1 1h2.5l2 8h7.5l1.5-6H4.5"/><circle cx="6.5" cy="12" r="1"/><circle cx="12" cy="12" r="1"/></svg></i></div>
</div>

<!-- Egg rolls -->
<div class="dish abs" style="left:74px;top:1622px">
  <h3>EGG ROLLS <small>(life changing)</small></h3>
  <div class="price" style="padding-left:8px">$10<small>for 10</small></div>
  <p>Our egg rolls are an experience not to be missed. They are provided either prepared and ready to cook or fresh and ready for pan frying at your convenience. We create a wonderfully balanced mix of prawn, chicken, and pork. We start by taking the time to properly Julian slice the carrots (slightly sweet), dry wood ear mushrooms (to enhance the texture), taro (an all-natural and healthy binder for the mix), onion, garlic, and glass noodles are all combined in a beautifully balanced mixture that is hand wrapped in Vietnamese rice paper.</p>
  <div class="order-btn">ADD TO ORDER<i><svg width="16" height="14" viewBox="0 0 16 14" fill="none" stroke="#fff" stroke-width="1.4"><path d="M1 1h2.5l2 8h7.5l1.5-6H4.5"/><circle cx="6.5" cy="12" r="1"/><circle cx="12" cy="12" r="1"/></svg></i></div>
</div>
<div class="dish-frame abs" style="left:617px;top:1631px">
  <div class="photo" role="img" aria-label="Photo of hand-wrapped rice paper rolls in a basket" style="background:var(--photo-rolls)"></div>
</div>

<!-- Crab soup -->
<div class="dish-frame abs" style="left:74px;top:2145px">
  <div class="photo" role="img" aria-label="Photo of a spoonful of thick crab and corn soup" style="background:var(--photo-crab)"></div>
</div>
<div class="dish abs" style="left:674px;top:2161px">
  <h3>CRAB SOUP <small>(mmm so good, so fresh)</small></h3>
  <div class="price">$ <span class="note">Market Price</span></div>
  <p>We use fresh whole chunk crab meat served in a thick homemade chicken and pork bone-based broth that takes 8 hours to prepare. Combined with whole quail eggs, sweet corn, asparagus, cilantro and cubed carrot all combine to present a medley of mouth-watering flavours that are simply a delightful seafood-based experience you won't want to miss.</p>
  <div class="order-btn">ADD TO ORDER<i><svg width="16" height="14" viewBox="0 0 16 14" fill="none" stroke="#fff" stroke-width="1.4"><path d="M1 1h2.5l2 8h7.5l1.5-6H4.5"/><circle cx="6.5" cy="12" r="1"/><circle cx="12" cy="12" r="1"/></svg></i></div>
</div>

<!-- Tuna -->
<div class="dish abs" style="left:74px;top:2621px">
  <h3>TUNA SALAD SANDWICH<br><small>(sweet, sour, and tangy)</small></h3>
  <div class="price">$9</div>
  <p>A succulently curated blend of tuna, pickle, lemon, onion, and celery that all combine to offer an experience you will say is sweet, sour, and tangy. Served with a carrot salad garnish. If you would like to kick this up a notch, we are happy to add our freshly sliced pepper of the day.</p>
  <div class="order-btn">ADD TO ORDER<i><svg width="16" height="14" viewBox="0 0 16 14" fill="none" stroke="#fff" stroke-width="1.4"><path d="M1 1h2.5l2 8h7.5l1.5-6H4.5"/><circle cx="6.5" cy="12" r="1"/><circle cx="12" cy="12" r="1"/></svg></i></div>
</div>
<div class="dish-frame abs" style="left:617px;top:2629px">
  <div class="photo" role="img" aria-label="Photo of a stacked tuna salad sandwich" style="background:var(--photo-sandwich)"></div>
</div>

<section class="contact abs" role="img" aria-label="Dimmed background photo of a noodle soup bowl">
  <h2>GET IN <span>TOUCH</span></h2>
  <h3>QUESTIONS?</h3>
  <a>hi@brimbowl.com.au</a>
</section>

<footer>
  <div class="foot-brand abs">BrimBowl</div>
  <nav class="foot-nav abs">
    <span class="active">Home</span><span>About Us</span><span>Menus</span><span>Blog</span><span>FAQ</span><span>Contact Us</span>
  </nav>
  <div class="social abs" aria-label="Social links"><span></span><span></span><span></span><span></span></div>
  <div class="copyright abs">© 2020 &nbsp;|&nbsp; www.companyname.com</div>
</footer>

</body>
</html>
```